Quelindra - Step Into Bloom! Business Card

We are bringing an amazing new system of dance to Australia and need a nifty, eye-catching little card that we can give to everyone to get them to come to class.

It needs a bit of information about Quelindra, along with contact details and a space for us to write a note for people about the next class.

Target Market(s)

30+ people that enjoy dance and are interested in self-development, meeting people and getting more out of life.

Industry/Entity Type

Business

Requirements
Must have
• Double sided in colour

A beautiful, simple design that indicates movement and is modern, fresh and uplifting.

The attached Quelindra logo

Text for the front :

Quelindra - the Step Into Bloom

Dance from your heart and feel your life open.

Regular classes in Sydney and Canberra with Maren Hollis and Ernesto Varga

Text for the back :

Quelindra ignites our vital spark for life and awakens our innate potential for pleasurable, joyful, heartfelt living through dance, music and authentic connection.

Ernesto and Maren are committed to offering authentic, supportive and inspiring spaces for your growth through Quelindra.

Contact us on maren@quelindra.com.au - evtrusk@zentromail.net or 0472 318 904.

www.quelindra.com.au

Nice to have
• Some movement in the design

Use some of the photos attached in some form - could be faded, incorporated into design etc.

Creative use of the logo - integrating it within the design - e.g perhaps using it as the O in Quelindra,
Should not have
• Not a lot of black

```html
<!DOCTYPE html>
<html lang="en">
<head>
<meta charset="utf-8">
<title>Quelindra – Business Card</title>
<link rel="stylesheet" href="https://fonts.googleapis.com/css2?family=Pacifico&family=Oranienbaum&display=swap">
<style>
  :root {
    --stage-light: #e4e4e4;
    --stage-dark: #9a9a9a;
    --plum: #7b0a6b;
    --plum-deep: #6a0760;
    --sky: #0b7bdc;
    --sky-edge: #3a8fe0;
    --crimson: #d0044e;
    --title-blue: #1c78cc;
    --link-blue: #1a86e8;
    --white: #ffffff;
  }
  * { box-sizing: border-box; margin: 0; padding: 0; }
  html, body { width: 1200px; height: 900px; overflow: hidden; }
  body {
    position: relative;
    background: radial-gradient(ellipse at 50% 40%, var(--stage-light) 0%, #c4c4c4 50%, var(--stage-dark) 100%);
    font-family: Arial, Helvetica, sans-serif;
  }
  .card { position: absolute; left: 260px; width: 680px; overflow: hidden; }

  /* Front */
  .card--front { top: 35px; height: 390px; background: var(--plum); }
  .front-photo {
    position: absolute; left: 250px; top: 0; width: 430px; height: 390px;
    background:
      linear-gradient(90deg, var(--plum) 0%, rgba(123,10,107,0.55) 22%, rgba(123,10,107,0) 45%),
      linear-gradient(160deg, #3a2a2a 0%, #6b4a3e 35%, #c9b8b0 55%, #8a6a5a 75%, #4a3430 100%);
  }
  .brand-seal {
    position: absolute; left: 20px; top: 15px; width: 121px; height: 121px;
    border-radius: 50%; background: var(--white);
    display: flex; align-items: center; justify-content: center;
  }
  .brand-seal__name {
    font-family: 'Oranienbaum', Georgia, serif; font-size: 24px; color: var(--plum);
  }
  .front-script {
    position: absolute; left: 140px; top: 100px;
    font-family: 'Pacifico', cursive; font-size: 36px; color: var(--crimson);
    line-height: 1; white-space: nowrap;
  }
  .front-title {
    position: absolute; left: 28px; top: 138px;
    font-family: 'Oranienbaum', Georgia, serif; font-size: 68px; color: var(--title-blue);
    line-height: 1; transform: scaleX(0.85); transform-origin: left;
  }
  .front-tagline {
    position: absolute; left: 30px; top: 218px;
    font-family: 'Pacifico', cursive; font-size: 17px; color: var(--white); white-space: nowrap;
  }
  .front-classes {
    position: absolute; left: 162px; top: 308px;
    font-size: 16px; color: var(--link-blue); white-space: nowrap;
  }
  .front-teachers {
    position: absolute; left: 142px; top: 336px;
    font-family: 'Pacifico', cursive; font-size: 20px; color: var(--white); white-space: nowrap;
  }

  /* Back */
  .card--back { top: 475px; height: 388px; background: var(--sky); border: 1px solid var(--sky-edge); }
  .back-photo {
    position: absolute; left: 0; top: 0; width: 240px; height: 388px;
    background:
      linear-gradient(90deg, rgba(11,123,220,0) 0%, rgba(11,123,220,0.35) 60%, var(--sky) 100%),
      linear-gradient(180deg, #a08a80 0%, #c9c2bc 40%, #6c7b98 70%, #3a3a44 100%);
  }
  .back-about {
    position: absolute; left: 0; right: 0; top: 58px;
    text-align: center; font-style: italic; font-size: 14.5px; line-height: 18px; color: var(--white);
  }
  .back-about p + p { margin-top: 17px; }
  .back-contact { position: absolute; left: 0; right: 0; top: 170px; text-align: center; padding-left: 20px; }
  .back-contact__heading {
    font-family: 'Pacifico', cursive; font-size: 21px; color: var(--crimson); margin-bottom: 0;
  }
  .back-contact__list { list-style: none; font-size: 22px; line-height: 27px; color: var(--white); }
  .back-web {
    position: absolute; left: 0; right: 0; top: 357px; padding-left: 20px;
    text-align: center; font-size: 15px; color: var(--crimson);
  }
</style>
</head>
<body>
  <section class="card card--front">
    <div class="front-photo" role="img" aria-label="Photo of a smiling couple dancing together in a studio"></div>
    <div class="brand-seal"><span class="brand-seal__name">Quelindra</span></div>
    <h1 class="front-title">Quelindra</h1>
    <p class="front-script">the Step Into Bloom</p>
    <p class="front-tagline">Dance from your heart and feel your life open</p>
    <p class="front-classes">Regular classes in Sydney and Canberra</p>
    <p class="front-teachers">with Maren Hollis and Ernesto Varga</p>
  </section>

  <section class="card card--back">
    <div class="back-photo" role="img" aria-label="Faded photo of two dancers embracing beside a brick wall"></div>
    <div class="back-about">
      <p>Quelindra ignites our vital spark for life and awakens our innate potential for pleasurable,<br>joyful, heartfelt living through dance, music and authentic connection.</p>
      <p>Ernesto and Maren are committed to offering authentic,<br>supportive and inspiring spaces for your growth through Quelindra.</p>
    </div>
    <div class="back-contact">
      <h2 class="back-contact__heading">Contact us :</h2>
      <ul class="back-contact__list">
        <li>maren@quelindra.com.au</li>
        <li>evtrusk@zentromail.net</li>
        <li>0472 318 904.</li>
      </ul>
    </div>
    <p class="back-web">www.quelindra.com.au</p>
  </section>
</body>
</html>
```